Revolutionary Digital Car Parking Ticket

We are looking for a Brochure Type Web design and a design for a Logo for a brand new company and a product that has no equal anywhere in the world. The product is subject to a Patent Application.
The Company is Bellwether Kerbside Limited and will have a URL of www.lonmeroto.com.au
The designs need to be in Adobe Photo Shop and we are seeking the actual adobe file with unmerged layers.
The product is a digital parking ticket which automatically identifies where a car is parked and if applicable automatically bills the user of the device for the cost of parking for the time the vehicle is parked. The user no longer needs to worry about parking fines, or “feeding” the parking metre. Equally there is no longer any need for those ugly street parking metres.
A picture of the device is attached.
The design needs to impart to the user of the Web Site a feeling of a company which is innovative, designing cutting edge technology, very smart, friendly and sensitive to peoples needs in its area of technology development.
Equally the site needs to be:
a) very simple, uncluttered and clean;
b) such that any user intuitively understands how to use and get what they want.
c) such that the user again intuitively trust the product and the company to deliver a product which does what it indicates it can do;
d) such that it provides confidence that the use of the product will save them money and make sure they don’t get parking fines again and are only charged for the time that they are parked; and
e) such that all understand that they are in control of the operation of the product.
The front page of the Web site needs to provide the user with the following access points:
a) Buy a product;
b) Log into their established account;
c) Make contact with the company;
d) Understand all of the Company Privacy Conditions; and
e) Understand who the company is.
Updates
Please remember that the product is about car parking in any place and one needs to ensure that a site user immediately recognises that by buying the device it makes Car Parking much easier. To put this another way the graphics on the site need to immediately let the user know we are on about car parking made easy.
Target Market(s)
Consumers. Ordinary people who drive cars
Industry/Entity Type
Digital
Logo Text
Ever Calm Tidy Motoring
Number of Pages Required
1 page
Font styles to use
Requirements
Must have
- Must be simple and clean and uncluttered
Nice to have
- Nil
Should not have
- Must not be cluttered

```html
<!DOCTYPE html>
<html lang="en">
<head>
<meta charset="utf-8">
<title>lonmeroto – Car Parking Made Easy</title>
<link href="https://fonts.googleapis.com/css2?family=Open+Sans:wght@400;600;700;800&display=swap" rel="stylesheet">
<style>
:root{
  --brand:#5b5cb1;
  --ink:#2b2b2b;
  --text:#3a3a3a;
  --muted:#777;
  --dark:#333333;
  --tile:#2e2e2e;
  --device:#4a4e52;
  --white:#ffffff;
}
*{margin:0;padding:0;box-sizing:border-box}
html,body{width:669px;height:1200px;overflow:hidden;background:var(--white);font-family:"Open Sans",Arial,sans-serif;color:var(--text)}
.page{position:relative;width:669px;height:1200px}
.site-header{position:absolute;left:0;top:0;width:669px;height:72px;display:flex;align-items:center;padding:0 30px}
.brand{display:flex;align-items:center;gap:8px;font-size:24px;font-weight:400;color:var(--brand);width:175px}
.brand-mark{width:18px;height:18px;border-radius:50%;background:var(--brand)}
.main-nav{display:flex;gap:20px;font-size:7px;font-weight:600;color:var(--ink);letter-spacing:.3px}
.main-nav .active{color:var(--brand)}
.header-tools{margin-left:auto;display:flex;gap:14px;align-items:center}
.login-link{font-size:7px;font-weight:600;color:var(--brand);letter-spacing:.3px}
.tool-dot{width:10px;height:10px;border-radius:50%;background:var(--brand)}
.hero{position:absolute;left:0;top:72px;width:669px;height:291px;background:#f2f2f2}
.hero-photo{position:absolute;left:0;top:0;width:669px;height:291px;
  background:
    radial-gradient(ellipse 210px 120px at 420px 110px,#f6f6f6 0%,#e8e8e8 60%,rgba(232,232,232,0) 100%),
    radial-gradient(ellipse 330px 190px at 380px 120px,var(--device) 0%,#5a5e62 60%,rgba(90,94,98,0) 100%),
    linear-gradient(135deg,#f7f7f7 0%,#e6e6e6 60%,#d6d6d6 100%)}
.hero-copy{position:absolute;left:50px;top:170px;color:var(--ink)}
.hero-copy h2{font-size:17px;font-weight:700;letter-spacing:.5px}
.hero-copy p{font-size:13px;line-height:15px;color:#555;width:130px;margin-top:2px}
.newsletter{position:absolute;left:0;top:363px;width:669px;height:70px;background:var(--brand);display:flex;align-items:center;justify-content:center;gap:22px}
.newsletter h3{color:var(--white);font-size:12px;font-weight:400;text-align:center;line-height:14px;letter-spacing:.5px}
.newsletter-form{display:flex}
.newsletter-form span{display:block;width:96px;height:18px;background:var(--white);font-size:6px;padding:5px 6px;color:#555}
.newsletter-form b{display:block;width:54px;height:18px;background:var(--dark);color:var(--white);font-size:6px;font-weight:600;text-align:center;line-height:18px}
.rule{position:absolute;left:0;width:669px;height:9px;background:var(--dark)}
.section-title{position:absolute;left:50px;font-size:29px;font-weight:800;color:var(--ink);letter-spacing:.5px}
.lead{position:absolute;left:50px;width:575px;font-size:11.5px;line-height:14px;color:var(--text)}
.product-photo{position:absolute;left:50px;top:618px;width:250px;height:112px;
  background:
    radial-gradient(ellipse 90px 38px at 140px 72px,#f3f3f3 0%,#e4e4e4 70%,rgba(228,228,228,0) 100%),
    radial-gradient(ellipse 120px 52px at 130px 58px,var(--device) 0%,#5a5e62 70%,rgba(90,94,98,0) 100%),
    #f4f4f4}
.product-info{position:absolute;left:325px;top:620px;width:300px}
.product-info p{font-size:7px;line-height:9px;color:var(--text)}
.price{font-size:15px;font-weight:700;color:var(--ink);margin-top:14px}
.cart-btn{display:inline-block;margin-top:24px;background:var(--dark);color:var(--white);font-size:6px;padding:5px 10px}
.tiles{position:absolute;left:50px;top:910px;width:570px;height:80px;display:flex;gap:5px}
.tiles div{flex:1;background:var(--tile)}
.site-footer{position:absolute;left:0;top:1003px;width:669px;height:165px;background:var(--brand);display:flex;padding:22px 50px 0}
.footer-col{color:var(--white);font-size:7px;line-height:17px}
.footer-col h4{font-size:8px;font-weight:400;color:#d6d6f2;margin-bottom:4px}
.col-sitemap{width:150px}.col-location{width:155px}.col-contact{width:165px}
.social-row{display:flex;gap:12px;margin-top:8px}
.social-row i{width:9px;height:9px;border-radius:50%;background:var(--white);display:block}
.copyright{position:absolute;left:0;top:1168px;width:669px;height:32px;text-align:center;font-size:6px;line-height:32px;color:var(--muted)}
</style>
</head>
<body>
<div class="page">
  <header class="site-header">
    <div class="brand"><span class="brand-mark"></span>lonmeroto</div>
    <nav class="main-nav">
      <span class="active">HOME</span><span>ABOUT</span><span>TECHNOLOGY</span><span>PRODUCT</span><span>CONTACT</span>
    </nav>
    <div class="header-tools">
      <span class="login-link">LOGIN</span>
      <svg width="11" height="11" viewBox="0 0 11 11" aria-label="Search"><circle cx="4.5" cy="4.5" r="3.5" fill="none" stroke="#5b5cb1" stroke-width="1.4"/><line x1="7" y1="7" x2="10.5" y2="10.5" stroke="#5b5cb1" stroke-width="1.4"/></svg>
      <span class="tool-dot"></span><span class="tool-dot"></span><span class="tool-dot"></span>
    </div>
  </header>

  <section class="hero">
    <div class="hero-photo" role="img" aria-label="Close-up photo of the grey and white digital car parking ticket device with its red stop and green start parking buttons"></div>
    <div class="hero-copy">
      <h2>OUR VISION</h2>
      <p>To help our customers realize their potential through the use of technology</p>
    </div>
  </section>

  <section class="newsletter">
    <h3>RECEIVE OUR<br>NEWSLETTER</h3>
    <div class="newsletter-form"><span>*Email</span><b>SEND</b></div>
  </section>
  <div class="rule" style="top:433px"></div>

  <h2 class="section-title" style="top:462px">OUR PRODUCT</h2>
  <p class="lead" style="top:508px">Lorem ipsum dolor sit amet, consectetur adipiscing elit, sed do eiusmod tempor incididunt ut labore et dolore magna aliqua. Ut enim ad minim veniam, quis nostrud exercitation ullamco laboris nisi ut aliquip ex ea commodo consequat.</p>
  <div class="product-photo" role="img" aria-label="Product photo of the digital car parking ticket device"></div>
  <div class="product-info">
    <p>Excepteur sint occaecat cupidatat non proident, sunt in culpa qui officia deserunt mollit anim id est laborum. Excepteur sint occaecat cupidatat non proident, sunt in culpa qui officia deserunt mollit anim id est laborum.</p>
    <div class="price">$ 98.00</div>
    <span class="cart-btn">Add to cart</span>
  </div>
  <div class="rule" style="top:740px"></div>

  <h2 class="section-title" style="top:776px">ABOUT US</h2>
  <p class="lead" style="top:820px">Lorem ipsum dolor sit amet, consectetur adipiscing elit, sed do eiusmod tempor incididunt ut labore et dolore magna aliqua. Ut enim ad minim veniam, quis nostrud exercitation ullamco laboris nisi ut aliquip ex ea commodo consequat. Lorem ipsum dolor sit amet, consectetur adipiscing elit, sed do eiusmod tempor incididunt ut labore et dolore magna aliqua. Ut enim ad minim veniam, quis nostrud exercitation ullamco laboris nisi ut aliquip ex ea commodo consequat</p>
  <div class="tiles"><div></div><div></div><div></div><div></div></div>

  <footer class="site-footer">
    <div class="footer-col col-sitemap"><h4>SITE MAP</h4>Home<br>About<br>Technology<br>Product<br>Contact<br>Privacy</div>
    <div class="footer-col col-location"><h4>Location</h4>123 XYZ Ave.<br>NY<br>USA</div>
    <div class="footer-col col-contact"><h4>Contact Us</h4>hello@lonmeroto.com.au<br>+234 123 123<br>+234 123 123</div>
    <div class="footer-col"><h4>Social</h4>Follow us on:<div class="social-row"><i></i><i></i><i></i></div></div>
  </footer>
  <div class="copyright">Copyright Lonmeroto 2015 | All Rights Reserved</div>
</div>
</body>
</html>
```